New Web Design Project

New Roofing Website homepage mockup

Complete design document here: https://files.plorvex.net/doc/7tQmZrA2kLwP9xVbN4cYhE3sJdF8gUoR6iKe1nTy/edit?usp=sharing
Updates

Number of Pages Required

1 page

Font styles to use
Sans Serif

```html
<!DOCTYPE html>
<html lang="en">
<head>
<meta charset="utf-8">
<title>Keystone Roofing – Home</title>
<link href="https://fonts.googleapis.com/css2?family=Roboto:wght@400;500;700;900&display=swap" rel="stylesheet">
<style>
:root{
  --blue:#29a3de;
  --blue-dark:#1f8fc6;
  --ink:#1b1b1b;
  --body:#555;
  --grey:#808080;
  --bar:#9a9a9a;
  --footer:#5a5a5c;
  --light:#f1f1f1;
  --white:#fff;
}
*{margin:0;padding:0;box-sizing:border-box}
html,body{width:1200px;height:4325px;overflow:hidden}
body{font-family:'Roboto',sans-serif;color:var(--body);background:var(--white);position:relative}
/* header */
.header{position:absolute;top:0;left:0;width:1200px;height:113px;background:var(--white);border-bottom:1px solid #e5e5e5}
.topbar{position:absolute;left:335px;top:0;width:865px;height:40px;background:var(--bar);clip-path:polygon(18px 0,100% 0,100% 100%,0 100%);color:var(--white);font-size:15px;font-weight:500;display:flex;align-items:center;padding-left:40px}
.topbar .social{margin-left:auto;display:flex;gap:22px;padding-right:60px}
.dot{width:10px;height:10px;border-radius:50%;background:var(--white);display:inline-block}
.brand{position:absolute;left:89px;top:40px;display:flex;align-items:center;gap:8px;font-weight:700;font-size:21px;color:var(--blue);letter-spacing:.5px;white-space:nowrap}
.brand .mark{width:14px;height:14px;background:var(--blue);flex:none}
.nav{position:absolute;top:68px;right:89px;display:flex;gap:36px;font-size:16px;font-weight:500;color:#333}
.nav .active{color:var(--blue)}
/* hero */
.hero{position:absolute;top:113px;left:0;width:1200px;height:728px;background:linear-gradient(180deg,#b9d1ea 0%,#8a98a4 35%,#6f6a63 70%,#4b4a47 100%)}
.hero-title{position:absolute;top:293px;width:1200px;text-align:center;color:var(--white);font-weight:900;font-size:72px;line-height:66px;letter-spacing:-1px;text-shadow:0 2px 6px rgba(0,0,0,.35)}
.btn{display:inline-block;background:var(--blue);color:var(--white);font-weight:700;font-size:15px;text-transform:uppercase;padding:11px 19px;white-space:nowrap}
.hero .btn{position:absolute;top:438px;left:477px}
/* headings */
.sec-title{position:absolute;width:1200px;text-align:center;font-weight:700;font-size:38px;color:var(--ink);text-transform:uppercase}
.sec-title::after{content:"";display:block;width:50px;height:3px;background:var(--blue);margin:10px auto 0}
/* services */
.service{position:absolute;top:990px;width:503px;height:221px;color:var(--white);padding:40px 58px}
.service.install{left:89px;background:var(--blue)}
.service.repair{left:607px;background:var(--grey)}
.service h3{font-size:54px;font-weight:700;line-height:48px}
.service h4{font-size:21px;font-weight:400;margin-top:2px}
.service p{font-size:14px;line-height:22px;margin-top:18px;width:400px}
.service svg{position:absolute;right:42px;top:26px}
/* about */
.about-bg{position:absolute;top:1300px;left:0;width:570px;height:560px;background:linear-gradient(90deg,#f4f4f6,#fff)}
.about-photo{position:absolute;left:89px;top:1302px;width:444px;height:456px;background:linear-gradient(160deg,#8fb4d6 0%,#c9c9c9 40%,#6b6458 100%)}
.about-photo-inner{position:absolute;left:296px;top:1510px;width:237px;height:248px;border-left:10px solid var(--blue);border-top:10px solid var(--blue);background:linear-gradient(135deg,#9a9088,#7c7066)}
.about-text{position:absolute;left:608px;top:1403px;width:500px}
.eyebrow{color:var(--blue);font-size:17px;font-weight:500;text-transform:uppercase}
.about-text h2{font-size:40px;line-height:40px;color:var(--ink);font-weight:700;margin-top:12px;text-transform:uppercase}
.about-text h2::after{content:"";display:block;width:40px;height:3px;background:var(--blue);margin-top:12px}
.about-text p{font-size:15.5px;line-height:27px;margin-top:22px;width:495px}
/* types */
.types{position:absolute;top:1860px;left:0;width:1200px;height:480px;background:var(--blue)}
.types .sec-title{color:var(--white);top:82px}
.types .sec-title::after{background:var(--white)}
.roof{position:absolute;top:218px;width:184px;height:182px;border:1px solid rgba(255,255,255,.55);border-top:none}
.roof .img{position:absolute;left:9px;top:-60px;width:167px;height:190px}
.roof .ico{position:absolute;right:22px;top:110px;width:36px;height:36px;border-radius:50%;background:var(--blue);border:2px solid var(--white)}
.roof span{position:absolute;bottom:14px;width:100%;text-align:center;color:var(--white);font-size:21px;font-weight:700}
/* projects */
.proj{position:absolute;width:330px;height:230px}
.proj.overlay::after{content:"";position:absolute;inset:0;background:rgba(120,120,120,.55)}
.proj .cap{position:absolute;z-index:1;left:36px;top:34px;color:var(--white);font-weight:700;font-size:26px;line-height:26px}
.proj .cap small{display:block;font-size:20px;margin-left:0}
.proj .plus{position:absolute;z-index:1;right:0;bottom:0;width:53px;height:53px;background:var(--blue);color:var(--white);font-size:36px;text-align:center;line-height:52px;font-weight:500}
/* choose */
.choose{position:absolute;top:3090px;left:0;width:1200px;height:344px;background:linear-gradient(180deg,#e7e7e9,#f5f5f6)}
.choose .sec-title{top:80px}
.choose p{position:absolute;top:158px;width:1200px;text-align:center;font-size:16px;line-height:24px;color:#444}
.choose .btn{position:absolute;top:216px;left:408px;padding:14px 30px;font-size:15px}
/* testimonials */
.quote{position:absolute;top:3610px;left:190px;width:820px;text-align:center;font-size:15.5px;line-height:24px;color:#444;text-indent:24px}
.qmark{position:absolute;font-size:90px;color:#ddd;font-family:Georgia,serif;line-height:1}
.client{position:absolute;top:3750px;width:1200px;text-align:center}
.client .n{color:var(--blue);font-size:19px}
.client .p{color:var(--ink);font-size:19px;font-weight:500;margin-top:2px}
.dots{position:absolute;top:3815px;left:573px;display:flex;gap:8px}
.dots i{width:11px;height:11px;border-radius:50%;background:#ddd;display:block}
.dots i.on{background:var(--blue)}
/* footer */
.footer{position:absolute;top:3902px;left:0;width:1200px;height:423px;background:var(--footer);color:#eee}
.footer .brand{left:89px;top:180px;font-size:22px;color:var(--blue)}
.footer .brand .mark{width:16px;height:16px}
.col{position:absolute;top:92px;font-size:14.5px}
.col h5{font-size:18px;font-weight:700;color:var(--white);margin-bottom:8px;text-transform:uppercase}
.col li{list-style:none;line-height:28px}
.col .line{line-height:28px}
.email-in{width:236px;height:36px;background:#6c6c6e;color:#aaa;padding:9px 14px;font-size:14px;margin-top:16px}
.sub{display:inline-block;background:var(--blue);color:var(--white);font-weight:700;padding:9px 14px;margin-top:10px;font-size:15px}
.phone{color:var(--blue);font-size:27px;font-weight:500;margin-top:4px}
.footer .social{display:flex;gap:20px;margin-top:10px}
.footer .rule{position:absolute;top:364px;left:89px;width:1021px;height:1px;background:#777}
.copy{position:absolute;top:385px;width:1200px;text-align:center;font-size:14px}
.totop{position:absolute;left:1146px;top:340px;width:34px;height:34px;border-radius:50%;background:var(--blue)}
</style>
</head>
<body>

<header class="header">
  <div class="topbar">
    <svg width="16" height="14" viewBox="0 0 16 14" style="margin-right:8px"><path d="M8 0 0 7h2v7h4V9h4v5h4V7h2z" fill="#fff"/></svg>
    We Provide Complete Home Roofing Services.
    <div class="social"><i class="dot"></i><i class="dot"></i></div>
  </div>
  <div class="brand"><span class="mark"></span>KEYSTONE ROOFING</div>
  <nav class="nav">
    <span class="active">Home</span><span>Services</span><span>About Us</span><span>Types of Roofs</span><span>Recent Projects</span><span>Contact Us</span>
  </nav>
</header>

<section class="hero" role="img" aria-label="Photo of a large grey two-storey house with new roof and a curved stone driveway">
  <h1 class="hero-title">BUILT RIGHT,<br>BUILT TO LAST</h1>
  <span class="btn">Get an instant&nbsp; estimate</span>
</section>

<h2 class="sec-title" style="top:912px">Services</h2>
<div class="service install">
  <h3>Roof</h3><h4>Installation</h4>
  <p>Lorem Ipsum is simply dummy text of the printing and type-setting industry. Lorem Ipsum has been .</p>
  <svg width="110" height="96" viewBox="0 0 110 96" fill="none" stroke="#fff" stroke-width="4" stroke-linejoin="round"><path d="M55 6 104 30 55 54 6 30z"/><path d="M6 46 55 70 104 46"/><path d="M6 62 55 86 104 62"/></svg>
</div>
<div class="service repair">
  <h3>Roof</h3><h4>Repair</h4>
  <p>Lorem Ipsum is simply dummy text of the printing and type-setting industry. Lorem Ipsum has been .</p>
  <svg width="110" height="100" viewBox="0 0 110 100" fill="none" stroke="#fff" stroke-width="4" stroke-linejoin="round"><path d="M8 48 55 8 102 48"/><path d="M20 38v56h70V38"/><path d="M44 94V66h22v28"/><path d="M76 10h14v16"/></svg>
</div>

<div class="about-bg" role="img" aria-label="Faint technical drawing of a house in the background"></div>
<div class="about-photo" role="img" aria-label="Photo of roofers working on a white house with a pickup truck in the driveway"></div>
<div class="about-photo-inner" role="img" aria-label="Close-up photo of a curved shingle roof over an arched window"></div>
<div class="about-text">
  <div class="eyebrow">About Company</div>
  <h2>Professional<br>Roofing Contractors</h2>
  <p>After over a decade of general contracting, we continue to see a repetitive trend by the roof purchase process where homeowners are constantly left confused, nervous, and worried when they need a new roof. As one of the most important features of keeping your home safe, this is unacceptable. Keystone Roofing was created to break this trend.</p>
</div>

<section class="types">
  <h2 class="sec-title">Types of Roofs</h2>
  <div class="roof" style="left:110px"><div class="img" role="img" aria-label="Cedar shingle roof photo" style="background:linear-gradient(160deg,#d99a62,#b8693a)"></div><i class="ico"></i><span>Cedar</span></div>
  <div class="roof" style="left:310px"><div class="img" role="img" aria-label="Metal standing seam roof photo" style="background:linear-gradient(160deg,#c6dcec,#5f8fb5)"></div><i class="ico"></i><span>Metal</span></div>
  <div class="roof" style="left:508px"><div class="img" role="img" aria-label="Slate roof photo" style="background:linear-gradient(160deg,#6a6d70,#3c3e41)"></div><i class="ico"></i><span>Slate</span></div>
  <div class="roof" style="left:708px"><div class="img" role="img" aria-label="Asphalt shingle roof photo" style="background:linear-gradient(160deg,#5a5b5d,#2f3032)"></div><i class="ico"></i><span>Asphalt</span></div>
  <div class="roof" style="left:905px"><div class="img" role="img" aria-label="Rubber flat roof photo" style="background:linear-gradient(180deg,#9c8a80 0%,#6d7073 30%,#2b2d30 100%)"></div><i class="ico"></i><span>Rubber</span></div>
</section>

<h2 class="sec-title" style="top:2432px">Recent Projects</h2>
<div class="proj" style="left:89px;top:2519px;background:linear-gradient(180deg,#9fb4c6,#7c7d78 60%,#3e3e3c)" role="img" aria-label="Project photo of a grey house with driveway"></div>
<div class="proj" style="left:434px;top:2519px;background:linear-gradient(180deg,#b5bcc4,#e8e8e8 50%,#5a5754)" role="img" aria-label="Project photo of a cupola with weathervane on a roof"></div>
<div class="proj" style="left:780px;top:2519px;background:linear-gradient(160deg,#c9d3db,#8a6650 55%,#6e5647)" role="img" aria-label="Project photo of cedar shake gable with arched window"></div>
<div class="proj" style="left:89px;top:2768px;background:linear-gradient(180deg,#3f5a36,#8b9aa4 50%,#4a4d50)" role="img" aria-label="Aerial project photo of a white house with dark roof"></div>
<div class="proj overlay" style="left:434px;top:2768px;background:linear-gradient(180deg,#9aa3a8,#6c6f72)" role="img" aria-label="Project photo of a residential roof">
  <div class="cap">Ridgefield,<small>MA</small></div><div class="plus">+</div>
</div>
<div class="proj" style="left:780px;top:2768px;background:linear-gradient(180deg,#2f4a2b,#d8d8d4 45%,#4e7a36)" role="img" aria-label="Aerial project photo of a white house with deck"></div>

<section class="choose" role="img" aria-label="Faded photo of roof framing in the background">
  <h2 class="sec-title">Choose Your Roof Type</h2>
  <p>A roof does more than keep the rain off your head. It protects your<br>biggest investment – your home.</p>
  <span class="btn">Calculate the cost of a new roof now</span>
</section>

<h2 class="sec-title" style="top:3552px">Happy Clients</h2>
<span class="qmark" style="left:184px;top:3596px">“</span>
<p class="quote">We needed to put a new roof on our house, as well as repair a sagging porch roof. Shingles had been flying off and we had had several leaks. Dan provided a very reasonable estimate - well below some of the other HomePro Directory companies. The work was done very promptly and professionally. A couple of issues that arose were settled to our satisfaction and Dan took full ownership of the situation. It was very clear that customer satisfaction is a priority for this company. I would definitely recommend and hire again</p>
<span class="qmark" style="left:806px;top:3700px">”</span>
<div class="client"><div class="n">Ellis</div><div class="p">Brookfield, MA</div></div>
<div class="dots"><i></i><i class="on"></i><i></i></div>

<footer class="footer">
  <div class="brand"><span class="mark"></span>KEYSTONE ROOFING</div>
  <div class="col" style="left:388px">
    <h5>Useful Links</h5>
    <ul><li>Keystone Roofing</li><li>Blog</li><li>Reviews</li><li>About</li><li>Services</li><li>Affiliations</li><li>Contact</li></ul>
  </div>
  <div class="col" style="left:582px">
    <h5>Newsletter</h5>
    <div class="line">Subscribe to our newsletter</div>
    <div class="email-in">Enter your email</div>
    <span class="sub">SUBSCRIBE</span>
  </div>
  <div class="col" style="left:863px">
    <h5>Contact Info</h5>
    <div class="line">48 Maple Ave.</div>
    <div class="line">Brookfield MA 01506</div>
    <div class="line">DanReyes@KeystoneRoofingMA.com</div>
    <div class="phone">555-014-2290</div>
    <div class="social"><i class="dot"></i><i class="dot"></i></div>
  </div>
  <div class="rule"></div>
  <div class="totop"><svg width="34" height="34" viewBox="0 0 34 34"><path d="M12 19l5-5 5 5" stroke="#fff" stroke-width="2" fill="none"/></svg></div>
  <div class="copy">Copyright 2020 | All Rights Reserved</div>
</footer>

</body>
</html>
```